brightmesh Business Card

Already have the logo, but now need the business card design

Industry/Entity Type

Business Software

Contact Information for Business Card

web site will be brightmesh.io / The card should have the person name / position / mobile / email / and company address

Colors

Designer to choose colors to be used in the design.

Requirements
Must have
• See business card details
• One side to have the brightmesh logo
Nice to have
• If possible the 'O' from flow can be watermarked into the second side
• Try to fit in the words brightmesh Business Solutions

```html
<!DOCTYPE html>
<html lang="en">
<head>
<meta charset="utf-8">
<title>brightmesh Business Card</title>
<link href="https://fonts.googleapis.com/css2?family=Arimo:wght@400;700&display=swap" rel="stylesheet">
<style>
  :root {
    --stage: #262626;
    --card: #1f1f20;
    --card-edge: #2a2a2b;
    --ink: #ffffff;
    --accent: #d8161b;
  }
  * { margin: 0; padding: 0; box-sizing: border-box; }
  html, body {
    width: 1200px;
    height: 1189px;
    overflow: hidden;
    background: var(--stage);
    font-family: "Arimo", Arial, sans-serif;
    color: var(--ink);
  }
  .sheet {
    width: 1200px;
    height: 1189px;
    display: flex;
    flex-direction: column;
    align-items: center;
    justify-content: center;
    gap: 56px;
  }
  .card {
    position: relative;
    width: 900px;
    height: 514px;
    border-radius: 34px;
    background: linear-gradient(160deg, var(--card-edge) 0%, var(--card) 55%);
    box-shadow: 0 14px 30px rgba(0,0,0,0.45);
    overflow: hidden;
  }

  /* Front side */
  .card-front .brand {
    position: absolute;
    left: 0; right: 0;
    top: 190px;
    text-align: center;
  }
  .wordmark {
    font-weight: 400;
    color: var(--ink);
    letter-spacing: -1px;
    line-height: 1;
  }
  .card-front .wordmark { font-size: 104px; }
  .card-front .website {
    display: block;
    margin-top: 12px;
    padding-left: 260px;
    font-size: 19px;
    letter-spacing: 2px;
    color: var(--accent);
  }

  /* Back side */
  .card-back .wordmark {
    position: absolute;
    left: 66px;
    top: 70px;
    font-size: 100px;
  }
  .rule-long {
    position: absolute;
    left: 92px;
    right: 66px;
    top: 322px;
    height: 3px;
    background: var(--accent);
  }
  .person {
    position: absolute;
    left: 92px;
    top: 250px;
  }
  .person-name {
    font-size: 30px;
    font-weight: 700;
    letter-spacing: 0.5px;
  }
  .person-role {
    font-size: 24px;
    color: var(--accent);
    margin-top: 0px;
  }
  .contact {
    position: absolute;
    left: 92px;
    top: 350px;
    list-style: none;
  }
  .contact li {
    display: flex;
    align-items: center;
    gap: 14px;
    font-size: 26px;
    margin-bottom: 12px;
  }
  .contact svg { width: 34px; height: 34px; flex: none; }
  .address {
    position: absolute;
    right: 70px;
    top: 348px;
    font-size: 24px;
    line-height: 1.35;
    font-style: normal;
  }
</style>
</head>
<body>
<main class="sheet">

  <section class="card card-front" aria-label="Card front">
    <div class="brand">
      <div class="wordmark">brightmesh</div>
      <span class="website">www.brightmesh.io</span>
    </div>
  </section>

  <section class="card card-back" aria-label="Card back">
    <div class="wordmark">brightmesh</div>

    <div class="person">
      <div class="person-name">Daniel Reeve</div>
      <div class="person-role">Founder</div>
    </div>

    <div class="rule-long"></div>

    <ul class="contact">
      <li>
        <svg viewBox="0 0 34 34" aria-hidden="true">
          <circle cx="17" cy="17" r="15" fill="none" stroke="#d8161b" stroke-width="2"/>
          <path d="M12 9.5c-1.5 1-2 2.8-1 5 1.6 3.6 4.4 6.6 8 8.3 2 .9 3.7.4 4.8-1.1l-2.7-2.6-2 1.2c-1.9-1-3.6-2.8-4.6-4.7l1.2-2-2.6-2.8z" fill="#d8161b"/>
        </svg>
        <span>(555) 014-2290</span>
      </li>
      <li>
        <svg viewBox="0 0 34 34" aria-hidden="true">
          <circle cx="17" cy="17" r="15" fill="none" stroke="#d8161b" stroke-width="2"/>
          <rect x="9" y="11.5" width="16" height="11" rx="1" fill="#d8161b"/>
          <path d="M9.5 12l7.5 6 7.5-6" fill="none" stroke="#1f1f20" stroke-width="1.6"/>
        </svg>
        <span>info@brightmesh.io</span>
      </li>
    </ul>

    <address class="address">
      PO BOX 48 Harbour Lane<br>
      7th street Geelong
    </address>
  </section>

</main>
</body>
</html>
```